Dating Coach needs a Book Cover Design

My new book called "Where the Lanterns Gather: Meeting Someone Worth Knowing in a Crowded Digital Age" needs a cover! I tried to make one on my own, but it's just not my skill set :) Please see attached for my best attempt. I'd like to see the title smaller and the tagline bigger - so that the tagline is easier to read. But I'm not sure how to do this and still have the Title look great. I'm also considering if the "WHERE LANTERNS GATHER" part should not be in all caps. Looking forward to your ideas! I'm also afraid that the drawing is a bit too cartoonish and doesn't match my brand. I'm looking for something elegant and also very approachable and down to earth. My website is www.gretavondlecounsel.example so you can use as reference! Please see my attached brand style guide for colors. This will be an e-book that I give away for free to anyone who signs up for my newsletter. Some mock-ups would also be great to use in advertising.

```html
<!DOCTYPE html>
<html lang="en">
<head>
<meta charset="UTF-8">
<title>Where Lanterns Gather — Book Cover</title>
<link rel="stylesheet" href="https://fonts.googleapis.com/css2?family=Barlow+Condensed:wght@500;600;700&family=Oswald:wght@600&display=swap">
<style>
  :root {
    --backdrop: #546f7a;
    --paper: #f2efe7;
    --title-red: #e0301f;
    --ink-slate: #22394a;
    --band-teal: #2e6c7c;
    --band-text: #f4f1ea;
    --art-red: #e23a22;
    --art-orange: #f0743a;
    --art-sand: #f1c98e;
  }
  * { box-sizing: border-box; margin: 0; padding: 0; }
  html, body {
    width: 1194px;
    height: 1200px;
    overflow: hidden;
    background: var(--backdrop);
  }
  .stage {
    position: relative;
    width: 1194px;
    height: 1200px;
    display: flex;
    align-items: center;
    justify-content: center;
  }
  .cover {
    position: relative;
    width: 760px;
    height: 1100px;
    background: var(--paper);
    overflow: hidden;
  }
  .cover-header {
    position: absolute;
    top: 70px;
    left: 30px;
    right: 30px;
    display: flex;
    flex-direction: column;
    align-items: center;
    text-align: center;
  }
  .series-label {
    font-family: "Barlow Condensed", sans-serif;
    font-weight: 600;
    font-size: 34px;
    letter-spacing: 1px;
    color: var(--ink-slate);
    text-transform: uppercase;
  }
  .book-title {
    margin-top: 6px;
    font-family: "Oswald", sans-serif;
    font-weight: 600;
    font-size: 90px;
    line-height: 1.02;
    color: var(--title-red);
    text-transform: uppercase;
    white-space: nowrap;
  }
  .book-subtitle {
    margin-top: 18px;
    font-family: "Barlow Condensed", sans-serif;
    font-weight: 600;
    font-size: 40px;
    line-height: 1.12;
    color: var(--ink-slate);
    text-transform: uppercase;
  }
  .cover-art {
    position: absolute;
    left: 150px;
    top: 500px;
    width: 500px;
    height: 560px;
    border-radius: 44% 40% 18% 24% / 26% 30% 14% 16%;
    background:
      radial-gradient(ellipse at 30% 14%, var(--art-sand) 0%, rgba(241,201,142,0) 42%),
      linear-gradient(165deg, var(--art-orange) 0%, var(--art-red) 55%, #d8321f 100%);
  }
  .author-band {
    position: absolute;
    left: 0;
    top: 960px;
    width: 100%;
    height: 78px;
    background: var(--band-teal);
    display: flex;
    align-items: center;
    justify-content: center;
    font-family: "Barlow Condensed", sans-serif;
    font-weight: 600;
    font-size: 32px;
    letter-spacing: 8px;
    color: var(--band-text);
    text-transform: uppercase;
  }
</style>
</head>
<body>
  <main class="stage">
    <article class="cover">
      <header class="cover-header">
        <p class="series-label">Modern Coaching</p>
        <h1 class="book-title">Where Lanterns<br>Gather</h1>
        <p class="book-subtitle">Meeting Someone Worth Knowing<br>in a Crowded Digital Age</p>
      </header>
      <div class="cover-art" role="img" aria-label="Illustration of a tall, scattered pile of red, orange and cream envelopes"></div>
      <div class="author-band">By Greta Vondle</div>
    </article>
  </main>
</body>
</html>
```